Modern Business Card Design for Independent Urban Music Label

We need a card design for an independent urban music label called Copper Kite Records based in London. We develop and promote urban British music artists. We attend lots of high profile events with high profile industry people and want a card that comes across both on-brand and sophisticated, professional, trustworthy. I have attached our logo - please use the black and orange version in the upper left HOWEVER we are open to seeing other colors than the orange used though we want the shape of the logo to remain the same.

Info to please include:
Name
Position
Phone
Email
Website

Additional Info:
Twitter: @CopperKiteRecsUK
Insta: @CopperKiteRecs

Target Market(s)

Industry professionals and others artists

Industry/Entity Type

Business

Contact Information for Business Card

Info to please include:
Name
Position
Phone
Email
Website

Additional Info:
Twitter: @CopperKiteRecsUK
Insta: @CopperKiteRecs

Requirements
Must have
• Logo, company name
• Info to please include:
• Name
• Position
• Phone
• Email
• Website
Nice to have
• Twitter: @CopperKiteRecsUK
• Insta: @CopperKiteRecs
• If it can be done so that it doesn't look cluttered

```html
<!DOCTYPE html>
<html lang="en">
<head>
<meta charset="utf-8">
<title>Copper Kite Records – Business Card</title>
<link href="https://fonts.googleapis.com/css2?family=Josefin+Sans:wght@300;400;600&display=swap" rel="stylesheet">
<style>
  :root {
    --canvas: #d9d9db;
    --card-white: #ffffff;
    --card-dark: #262626;
    --ink: #1d1d1d;
    --ink-soft: #555555;
    --tagline: #e6e6e6;
    --orange: #f5901e;
    --red-light: #f4511c;
    --red: #d91f16;
    --red-deep: #a8120f;
    --icon-phone: #1d1d1d;
    --icon-mail: #3db54a;
    --icon-web: #3b4fa8;
    --icon-social-a: #2aa6de;
    --icon-social-b: #8b3a9c;
  }
  * { box-sizing: border-box; margin: 0; padding: 0; }
  html, body { width: 1200px; height: 834px; overflow: hidden; }
  body {
    background: var(--canvas);
    font-family: "Josefin Sans", sans-serif;
    display: flex;
    flex-direction: column;
    align-items: center;
    justify-content: center;
    gap: 40px;
  }
  .card {
    position: relative;
    width: 640px;
    height: 366px;
    overflow: hidden;
    box-shadow: 0 6px 18px rgba(0,0,0,0.18);
  }
  .card--front { background: var(--card-white); }
  .card--back { background: var(--card-dark); }

  .card__band {
    position: absolute;
    left: 0; right: 0; bottom: 0;
    height: 92px;
    border-top: 6px solid var(--orange);
  }
  .card__band-gap {
    height: 6px;
    background: var(--card-white);
  }
  .card__band-fill {
    height: 80px;
    background: linear-gradient(100deg, var(--red-light) 0%, var(--red) 45%, var(--red-deep) 100%);
  }

  /* Front */
  .brand {
    position: absolute;
    left: 36px; top: 100px;
    width: 190px;
    display: flex;
    flex-direction: column;
    align-items: center;
    gap: 12px;
  }
  .brand__dot {
    width: 46px; height: 46px;
    border-radius: 50%;
    background: var(--orange);
  }
  .brand__name {
    color: var(--orange);
    font-weight: 600;
    font-size: 16px;
    letter-spacing: 1.5px;
    text-transform: uppercase;
    text-align: center;
  }
  .divider {
    position: absolute;
    left: 0; top: 0;
  }
  .contact {
    position: absolute;
    left: 300px; top: 40px;
  }
  .contact__name {
    font-size: 30px;
    font-weight: 600;
    font-variant: small-caps;
    letter-spacing: 2px;
    color: var(--ink);
    line-height: 1;
  }
  .contact__role {
    font-size: 14px;
    color: var(--ink-soft);
    margin: 2px 0 14px;
  }
  .contact__list { list-style: none; }
  .contact__item {
    display: flex;
    align-items: center;
    gap: 12px;
    font-size: 16px;
    color: var(--ink);
    height: 30px;
  }
  .contact__icon { width: 22px; height: 22px; flex: none; }

  /* Back */
  .back__brand {
    position: absolute;
    left: 0; right: 0; top: 62px;
    display: flex;
    flex-direction: column;
    align-items: center;
    gap: 12px;
  }
  .tagline {
    position: absolute;
    left: 0; right: 0; top: 196px;
    display: flex;
    align-items: center;
    justify-content: center;
    gap: 14px;
    color: var(--tagline);
    font-weight: 300;
    font-size: 21px;
    letter-spacing: 2px;
    text-transform: uppercase;
  }
  .tagline__rule {
    width: 26px;
    height: 10px;
    border-top: 1px solid var(--tagline);
    border-bottom: 1px solid var(--tagline);
    position: relative;
  }
  .tagline__rule::after {
    content: "";
    position: absolute;
    left: 0; right: 0; top: 3.5px;
    border-top: 1px solid var(--tagline);
  }
</style>
</head>
<body>

<section class="card card--front" aria-label="Business card front">
  <div class="brand">
    <span class="brand__dot"></span>
    <span class="brand__name">Copper Kite Records</span>
  </div>

  <svg class="divider" width="640" height="366" aria-hidden="true">
    <line x1="268" y1="40" x2="220" y2="250" stroke="#9a9a9a" stroke-width="1.2"/>
  </svg>

  <div class="contact">
    <p class="contact__name">Name Here</p>
    <p class="contact__role">Position</p>
    <ul class="contact__list">
      <li class="contact__item">
        <svg class="contact__icon" viewBox="0 0 22 22" aria-hidden="true">
          <circle cx="11" cy="11" r="11" fill="var(--icon-phone)"/>
          <path d="M6 9.5c0-2 2.2-3 5-3s5 1 5 3l-2 .6-.5-1.6c-1.6-.5-3.4-.5-5 0L8 10.1z" fill="#fff"/>
          <rect x="7.5" y="11" width="7" height="4.5" rx="1" fill="#fff"/>
        </svg>
        +123.456.789
      </li>
      <li class="contact__item">
        <svg class="contact__icon" viewBox="0 0 22 22" aria-hidden="true">
          <circle cx="11" cy="11" r="11" fill="var(--icon-mail)"/>
          <rect x="5.5" y="7" width="11" height="8" fill="#fff"/>
          <path d="M5.5 7l5.5 4.5L16.5 7" fill="none" stroke="var(--icon-mail)" stroke-width="1"/>
        </svg>
        youremail@domain.com
      </li>
      <li class="contact__item">
        <svg class="contact__icon" viewBox="0 0 22 22" aria-hidden="true">
          <circle cx="11" cy="11" r="11" fill="var(--icon-web)"/>
          <g fill="none" stroke="#fff" stroke-width="1">
            <circle cx="11" cy="11" r="6"/>
            <ellipse cx="11" cy="11" rx="2.6" ry="6"/>
            <line x1="5" y1="11" x2="17" y2="11"/>
            <line x1="6" y1="8" x2="16" y2="8"/>
            <line x1="6" y1="14" x2="16" y2="14"/>
          </g>
        </svg>
        http://www.copperkiterecords.co.uk/
      </li>
      <li class="contact__item">
        <svg class="contact__icon" viewBox="0 0 22 22" aria-hidden="true">
          <circle cx="11" cy="11" r="11" fill="var(--icon-social-a)"/>
        </svg>
        @CopperKiteRecsUK
      </li>
      <li class="contact__item">
        <svg class="contact__icon" viewBox="0 0 22 22" aria-hidden="true">
          <rect width="22" height="22" rx="5" fill="var(--icon-social-b)"/>
        </svg>
        @CopperKiteRecs
      </li>
    </ul>
  </div>

  <div class="card__band">
    <div class="card__band-gap"></div>
    <div class="card__band-fill" role="img" aria-label="Red and orange faceted triangle pattern band"></div>
  </div>
</section>

<section class="card card--back" aria-label="Business card back">
  <div class="back__brand">
    <span class="brand__dot"></span>
    <span class="brand__name">Copper Kite Records</span>
  </div>

  <p class="tagline">
    <span class="tagline__rule"></span>
    Independent Urban Music Label
    <span class="tagline__rule"></span>
  </p>

  <div class="card__band">
    <div class="card__band-gap"></div>
    <div class="card__band-fill" role="img" aria-label="Red and orange faceted triangle pattern band"></div>
  </div>
</section>

</body>
</html>
```